i would like a business card to leave with customers and potential customers for electrical work and for the supply and install of reverse cycle airconditioning in the domestic and commercial market.
I own my own business and im a sole trader. I have an a'class electrical lisence and also a refrigeration lisence so i am
able to offer complete installations in airconditioning by a fully qualified and lisenced tradesman.
im looking for something that comes across as unique and professional.
i had the coluor black and some gold in mind but open to any coluors.
something like Brightline Electrical & Refrigeration
or Brightline Air.
i will use this design on a business card to advertise through summer to help generate installs through the busy season.

Target Market(s)

Mainly domestic house holds through summer who are in need of airconditioning and reliable information to acomadate thier cooling and heating requirements

Industry/Entity Type

Electrical

Requirements
Must have
• Business name- Brightline
My name- Peter Mulvane
My mobile no- 0438 517 209
My email- rtmulvane@kestrelnet.com.au
Installation & Decomissioning of aiconditioning split systems
LIC NO: TKR 504613
Nice to have
• Brightline Electrical & Refrigeration

```html
<!DOCTYPE html>
<html lang="en">
<head>
<meta charset="utf-8">
<title>Brightline Electrical &amp; Refrigeration – Business Cards</title>
<link rel="stylesheet" href="https://fonts.googleapis.com/css2?family=Cormorant+Garamond:wght@500&family=Tinos:wght@400;700&family=PT+Sans&display=swap">
<style>
  :root {
    --black: #000000;
    --gold: #bf9a4e;
    --white: #ffffff;
    --grey: #6a6a6a;
    --divider: #ffffff;
    --serif: "Tinos", "Times New Roman", serif;
    --display: "Cormorant Garamond", Georgia, serif;
    --sans: "PT Sans", Arial, sans-serif;
  }
  * { margin: 0; padding: 0; box-sizing: border-box; }
  html, body { width: 1200px; height: 2979px; overflow: hidden; background: var(--black); }
  .sheet { position: relative; width: 1200px; height: 2979px; }
  .panel { position: absolute; left: 0; width: 1200px; overflow: hidden; }
  .panel--dark { background: var(--black); }
  .panel--grey { background: var(--grey); }
  .gap { position: absolute; left: 0; width: 1200px; background: var(--divider); }

  .side-text {
    position: absolute;
    writing-mode: vertical-rl;
    transform: rotate(180deg);
    font-family: var(--serif);
    color: var(--white);
    text-align: center;
    white-space: nowrap;
    line-height: 1.1;
  }
  .rule { position: absolute; left: 397px; width: 3px; background: var(--white); }

  .wordmark {
    position: absolute; left: 0; width: 1200px; text-align: center;
    font-family: var(--display); font-weight: 500; color: var(--gold);
    letter-spacing: 4px; line-height: 1;
  }
  .wordmark--front { left: 420px; width: 780px; }
  .wordmark--bold { font-family: var(--serif); font-weight: 700; letter-spacing: 2px; }

  .tagline {
    position: absolute; left: 0; width: 1200px; text-align: center;
    font-family: var(--sans); color: var(--gold); font-size: 56px; line-height: 1;
  }

  .contact {
    position: absolute; left: 451px;
    font-family: var(--serif); color: var(--white); font-size: 44px; line-height: 1;
  }
  .contact--large { left: 451px; font-size: 46px; }

  .info-title, .info-line, .info-lic {
    position: absolute; left: 0; width: 1200px; text-align: center;
    font-family: var(--serif); color: var(--black); line-height: 1;
  }
  .info-title { font-size: 56px; }
  .info-line { font-size: 42px; }
  .info-lic { font-size: 52px; }
  .info-contact {
    position: absolute; left: 31px;
    font-family: var(--serif); color: var(--black); font-size: 42px; line-height: 1;
  }
</style>
</head>
<body>
<div class="sheet">

  <!-- Card one: front -->
  <section class="panel panel--dark" style="top:0;height:521px;">
    <div class="side-text" style="left:40px;top:10px;height:500px;font-size:31px;">Brightline Electrical &amp; Refrigeration</div>
    <div class="side-text" style="left:124px;top:40px;height:440px;font-size:28px;">Installation &amp; Decomissioning of<br>airconditioning split systems</div>
    <div class="side-text" style="left:252px;top:60px;height:400px;font-size:32px;">LIC NO: TKR 504613</div>
    <div class="rule" style="top:20px;height:480px;"></div>
    <div class="wordmark wordmark--front" style="top:40px;font-size:120px;">Brightline</div>
    <div class="contact" style="top:278px;">Peter Mulvane</div>
    <div class="contact" style="top:338px;">Mob.: 0438 517 209</div>
    <div class="contact" style="top:396px;">email: rtmulvane@kestrelnet.com.au</div>
  </section>

  <!-- Card one: back -->
  <section class="panel panel--dark" style="top:521px;height:501px;">
    <div class="wordmark" style="top:105px;font-size:150px;">Brightline</div>
    <div class="tagline" style="top:350px;">Brightline Electrical &amp; Refrigeration</div>
  </section>

  <div class="gap" style="top:1022px;height:20px;"></div>

  <!-- Card two: back -->
  <section class="panel panel--dark" style="top:1042px;height:444px;">
    <div class="wordmark" style="top:60px;font-size:150px;">Brightline</div>
    <div class="tagline" style="top:318px;">Brightline Electrical &amp; Refrigeration</div>
  </section>

  <!-- Card two: front -->
  <section class="panel panel--grey" style="top:1486px;height:462px;">
    <div class="info-title" style="top:46px;">Brightline Electrical &amp; Refrigeration</div>
    <div class="info-line" style="top:118px;">Installation &amp; Decomissioning of airconditioning split systems</div>
    <div class="info-lic" style="top:175px;">LIC NO: TKR 504613</div>
    <div class="info-contact" style="top:294px;">Peter Mulvane</div>
    <div class="info-contact" style="top:346px;">Mob.: 0438 517 209</div>
    <div class="info-contact" style="top:398px;">email: rtmulvane@kestrelnet.com.au</div>
  </section>

  <!-- Card three: front -->
  <section class="panel panel--dark" style="top:1948px;height:521px;">
    <div class="side-text" style="left:40px;top:10px;height:500px;font-size:31px;">Brightline Electrical &amp; Refrigeration</div>
    <div class="side-text" style="left:124px;top:40px;height:440px;font-size:28px;">Installation &amp; Decomissioning of<br>airconditioning split systems</div>
    <div class="side-text" style="left:252px;top:60px;height:400px;font-size:32px;">LIC NO: TKR 504613</div>
    <div class="rule" style="top:20px;height:480px;"></div>
    <div class="wordmark wordmark--front wordmark--bold" style="top:100px;font-size:120px;">Brightline</div>
    <div class="contact contact--large" style="top:296px;">Peter Mulvane</div>
    <div class="contact contact--large" style="top:366px;">Mob.: 0438 517 209</div>
    <div class="contact contact--large" style="top:424px;">email: rtmulvane@kestrelnet.com.au</div>
  </section>

  <!-- Card three: back -->
  <section class="panel panel--dark" style="top:2469px;height:510px;border-top:3px solid var(--white);">
    <div class="wordmark wordmark--bold" style="top:95px;font-size:140px;">Brightline</div>
    <div class="tagline" style="top:340px;">Brightline Electrical &amp; Refrigeration</div>
  </section>

</div>
</body>
</html>
```